The Lanternmoss Soiree Company Ltd. Needs a Facebook Design. An Event & Wedding Company

We need a WOW Facebook design. Focusing on catching people's attention. We don't want it all wedding like Facebook because we do want to focus on events too.

We currently have an underconstruction website up. feel free to check it out.

Http://www.thelanternmosssoiree.example

An attachment of our logo is attached below

Be Creative!!

Target Market(s)

Companies & Couples who's getting married or engaged 

Industry/Entity Type

Wedding

Font styles to use
Serif
Sans Serif
Decorative
Script

Colors

Designer to choose colors to be used in the design.

Requirements
Must have
• VERY VERY CREATIVE! CATCHY!
Should not have
• nothing really boring. anything green!

```html
<!DOCTYPE html>
<html lang="en">
<head>
<meta charset="utf-8">
<title>The Lanternmoss Soiree — Events &amp; Wedding</title>
<link rel="stylesheet" href="https://fonts.googleapis.com/css2?family=Poiret+One&display=swap">
<style>
  :root {
    --ink: #231f20;
    --paper: #ffffff;
    --frame: #2b2b2b;
    --gold: #c9a063;
    --rose: #e2197a;
    --scarlet: #d7262f;
    --blush: #f4a9a0;
    --peach: #e9b89a;
    --plum: #8c2f4f;
    --cocoa: #4a2a1f;
  }
  html, body {
    margin: 0;
    padding: 0;
    width: 1200px;
    height: 668px;
    overflow: hidden;
    background: var(--paper);
  }
  .cover {
    position: relative;
    width: 1200px;
    height: 668px;
    box-sizing: border-box;
    border: 2px solid var(--frame);
    background: var(--paper);
    overflow: hidden;
  }
  .lockup {
    position: absolute;
    left: 74px;
    top: 200px;
    width: 694px;
    font-family: "Poiret One", sans-serif;
    font-weight: 400;
    color: var(--ink);
    text-align: center;
  }
  .lockup__rule-row {
    display: flex;
    align-items: center;
    gap: 22px;
    height: 56px;
  }
  .lockup__rule {
    flex: 1;
    height: 1.5px;
    background: var(--ink);
  }
  .lockup__article {
    font-size: 30px;
    line-height: 1;
    letter-spacing: 0.04em;
  }
  .lockup__dot {
    width: 16px;
    height: 16px;
    border-radius: 50%;
    background: var(--gold);
  }
  .lockup__name {
    margin: 14px 0 0;
    font-size: 56px;
    font-weight: 400;
    letter-spacing: 0.12em;
    padding-left: 0.12em;
    text-transform: uppercase;
    line-height: 1;
    white-space: nowrap;
  }
  .lockup__tagline {
    margin: 30px 0 22px;
    font-size: 26px;
    font-weight: 400;
    letter-spacing: 1.05em;
    padding-left: 1.05em;
    text-transform: uppercase;
    line-height: 1;
    white-space: nowrap;
  }
  .floral-cascade {
    position: absolute;
    right: 0;
    top: 0;
    width: 420px;
    height: 100%;
    background: linear-gradient(180deg,
      var(--rose) 0%,
      var(--blush) 22%,
      var(--scarlet) 38%,
      var(--peach) 58%,
      var(--scarlet) 72%,
      var(--plum) 86%,
      var(--rose) 100%);
    -webkit-mask-image: linear-gradient(90deg, transparent 0%, #000 35%);
    mask-image: linear-gradient(90deg, transparent 0%, #000 35%);
    opacity: 0.85;
  }
</style>
</head>
<body>
  <main class="cover">
    <section class="lockup">
      <div class="lockup__rule-row">
        <span class="lockup__rule"></span>
        <span class="lockup__article">The</span>
        <span class="lockup__rule"></span>
      </div>
      <h1 class="lockup__name">Lanternmoss Soiree</h1>
      <p class="lockup__tagline">Events &amp; Wedding</p>
      <div class="lockup__rule-row">
        <span class="lockup__rule"></span>
        <span class="lockup__dot"></span>
        <span class="lockup__rule"></span>
      </div>
    </section>
    <div class="floral-cascade" role="img" aria-label="Illustration of pink, red, peach and plum flowers on curling brown vines with fluttering butterflies, cascading down the right edge"></div>
  </main>
</body>
</html>
```